VelaCure Wellness Business Cards

I am looking to have luxury business cards made for my IV Therapy and Wellness business.
Updates

Target Market(s)

Health and Wellness professionals

Industry/Entity Type

MedSpa

Contact Information for Business Card

Tobin Haverly, MSN, RN, CCRN Tobin@velacurewellness.com (916) 582-3179 QR code to website www.velacurewellness.com

```html
<!DOCTYPE html>
<html lang="en">
<head>
<meta charset="utf-8">
<title>VelaCure Wellness Business Cards</title>
<link href="https://fonts.googleapis.com/css2?family=Montserrat:wght@700;800&family=Open+Sans:wght@400;600;700&display=swap" rel="stylesheet">
<style>
  :root {
    --navy: #262a63;
    --sky: #1ba0d8;
    --ink-grey: #4d4f57;
    --card: #ffffff;
    --backdrop: #e9eaed;
  }
  * { box-sizing: border-box; margin: 0; padding: 0; }
  html, body { width: 1200px; height: 900px; overflow: hidden; }
  body {
    background: var(--backdrop);
    position: relative;
    font-family: "Open Sans", sans-serif;
  }
  .card {
    position: absolute;
    width: 660px;
    height: 377px;
    background: var(--card);
    box-shadow: 0 6px 22px rgba(0,0,0,0.12);
    overflow: hidden;
  }
  .card--front { left: 70px; top: 40px; }
  .card--back { left: 470px; top: 480px; }

  .brand {
    font-family: "Montserrat", sans-serif;
    font-weight: 800;
    color: var(--navy);
    display: flex;
    align-items: center;
    gap: 12px;
    white-space: nowrap;
  }
  .brand__dot {
    width: 18px; height: 18px;
    border-radius: 50%;
    background: var(--sky);
    flex: none;
  }

  /* Front */
  .card--front .brand {
    position: absolute;
    left: 0; right: 0; top: 112px;
    justify-content: center;
    font-size: 44px;
  }
  .hours {
    position: absolute;
    left: 0; right: 0; top: 208px;
    text-align: center;
    font-family: "Montserrat", sans-serif;
    font-weight: 700;
  }
  .hours__label { color: var(--sky); font-size: 19px; }
  .hours__time { color: var(--navy); font-size: 21px; margin-top: 4px; }
  .front-band {
    position: absolute;
    left: 270px; bottom: 0;
    width: 300px; height: 34px;
    background: var(--sky);
  }

  /* Back */
  .card--back .brand {
    position: absolute;
    right: 34px; top: 70px;
    font-size: 32px;
  }
  .side-bar {
    position: absolute;
    left: 0; top: 200px;
    width: 22px; height: 150px;
    background: var(--sky);
  }
  .contact {
    position: absolute;
    left: 58px; top: 168px;
  }
  .contact__name {
    font-weight: 700;
    color: var(--navy);
    font-size: 20px;
  }
  .contact__creds { font-weight: 400; font-size: 14px; color: var(--navy); }
  .contact__role { color: var(--ink-grey); font-size: 16px; margin-top: 2px; }
  .contact__list { list-style: none; margin-top: 18px; }
  .contact__item {
    display: flex; align-items: center; gap: 10px;
    color: var(--ink-grey); font-size: 15px;
    line-height: 24px;
  }
  .contact__item b { color: var(--navy); font-weight: 700; }
  .icon { width: 15px; height: 15px; flex: none; }
  .icon--solid { fill: var(--navy); }
  .icon--line { fill: none; stroke: var(--navy); stroke-width: 1.8; }
</style>
</head>
<body>

<section class="card card--front" aria-label="Card front">
  <div class="brand"><span class="brand__dot"></span>VelaCure Wellness</div>
  <div class="hours">
    <p class="hours__label">Our Hours</p>
    <p class="hours__time">Monday to Sunday 9am - 7pm</p>
  </div>
  <div class="front-band"></div>
</section>

<section class="card card--back" aria-label="Card back">
  <div class="brand"><span class="brand__dot"></span>VelaCure Wellness</div>
  <div class="side-bar"></div>
  <div class="contact">
    <p class="contact__name">Tobin Haverly, <span class="contact__creds">MSN, RN, CCRN</span></p>
    <p class="contact__role">Founder &amp; Clinical Director</p>
    <ul class="contact__list">
      <li class="contact__item">
        <svg class="icon icon--solid" viewBox="0 0 24 24"><path d="M6.6 10.8a15.1 15.1 0 0 0 6.6 6.6l2.2-2.2c.3-.3.7-.4 1-.2 1.1.4 2.3.6 3.6.6.6 0 1 .4 1 1V20c0 .6-.4 1-1 1A17 17 0 0 1 3 4c0-.6.4-1 1-1h3.5c.6 0 1 .4 1 1 0 1.3.2 2.5.6 3.6.1.3 0 .7-.2 1z"/></svg>
        (916) 582-3179
      </li>
      <li class="contact__item">
        <svg class="icon icon--line" viewBox="0 0 24 24"><rect x="2.5" y="5" width="19" height="14"/><path d="M3.5 6.5 12 13l8.5-6.5"/></svg>
        <span>Tobin@<b>VelaCureWellness</b>.com</span>
      </li>
      <li class="contact__item">
        <svg class="icon icon--line" viewBox="0 0 24 24"><circle cx="12" cy="12" r="9.5"/><ellipse cx="12" cy="12" rx="4.5" ry="9.5"/><path d="M2.5 12h19M4 7h16M4 17h16"/></svg>
        <span>www.<b>velacurewellness</b>.com</span>
      </li>
      <li class="contact__item">
        <svg class="icon icon--solid" viewBox="0 0 24 24"><path d="M12 2a7 7 0 0 0-7 7c0 5.2 7 13 7 13s7-7.8 7-13a7 7 0 0 0-7-7zm0 9.5A2.5 2.5 0 1 1 12 6.5a2.5 2.5 0 0 1 0 5z"/></svg>
        Corvell Springs, Ca
      </li>
    </ul>
  </div>
</section>

</body>
</html>
```